Trade Show Booth Sign Design for Retracting Banner

I need a trade show booth sign designed. It will be for a retractable banner that is double sided with 34 by 81 inch.

I want to incorporate my logo (see attached, have it in other file formats as well) and graphics from my website (https://www.dolbrookteachingadvisory.com/) with parts or all of the following text.

· Educational Content Creation
o Supplemental Textbook Content Development
o E-learning Content Development
· Curriculum Development
o KVTR/Bright Ladder
o Three Dimensional Learning
· Assessment
o Formative Assessments
o Elementary School, Middle School, High School, College, and Business
· Professional Development
o Training
o Facilitation

Target Market(s)

Education

Industry/Entity Type

Education

Font styles to use
Sans Serif

Colors

Designer to choose colors to be used in the design.

Requirements
Must have
• Eye catching and easy to read design
Nice to have
• Would like to see incorporation of my logo and some of the elements of my website images
Should not have
• N/A

```html
<!DOCTYPE html>
<html lang="en">
<head>
<meta charset="utf-8">
<title>Dolbrook Teaching Advisory – Retractable Banner Options</title>
<link rel="stylesheet" href="https://fonts.googleapis.com/css2?family=Oswald:wght@500;600;700&family=Open+Sans:wght@400&display=swap">
<style>
  :root {
    --board: #d4d5d7;
    --navy: #1e2659;
    --navy-deep: #1a2150;
    --white: #ffffff;
    --chalk: #2a2a2a;
    --orange: #f7a623;
    --red: #ec2a2c;
    --sky: #a9d8f7;
    --yellow: #ffd800;
    --url-blue: #3d8fd9;
    --label: #1a1a1a;
  }
  * { box-sizing: border-box; margin: 0; padding: 0; }
  html, body { width: 1200px; height: 848px; overflow: hidden; }
  body {
    background: var(--board);
    position: relative;
    font-family: "Oswald", "Arial Narrow", sans-serif;
  }
  .option-label {
    position: absolute;
    top: 30px;
    width: 294px;
    text-align: center;
    font-family: "Open Sans", Arial, sans-serif;
    font-size: 27px;
    color: var(--label);
  }
  .banner {
    position: absolute;
    top: 76px;
    width: 294px;
    height: 699px;
    background: var(--white);
    box-shadow: 0 1px 4px rgba(0,0,0,.25);
    overflow: hidden;
  }
  .banner--one   { left: 74px; }
  .banner--two   { left: 454px; }
  .banner--three { left: 846px; }
  .label--one   { left: 74px; }
  .label--two   { left: 454px; }
  .label--three { left: 846px; }

  .banner__head {
    position: relative;
    height: 200px;
    background: var(--white);
  }
  .banner--three .banner__head { background: var(--chalk); }

  .idea-bulbs {
    position: absolute;
    left: 6px; right: 6px; top: 0;
    height: 84px;
    background: linear-gradient(90deg,
      rgba(233,72,52,.28) 0%, rgba(96,128,214,.28) 25%,
      rgba(255,214,40,.32) 50%, rgba(247,140,40,.28) 72%,
      rgba(80,186,228,.28) 100%);
    border-radius: 0 0 20px 20px;
  }

  .brand {
    position: absolute;
    left: 0; right: 0; top: 98px;
    text-align: center;
    color: var(--navy);
    font-weight: 700;
    line-height: 1;
  }
  .banner--three .brand { color: var(--white); }
  .brand__name { display: block; font-size: 52px; letter-spacing: 1px; }
  .brand__tag  { display: block; font-size: 19px; margin-top: 4px; letter-spacing: .5px; }

  .services {
    position: relative;
    height: 422px;
    background: var(--navy);
    display: grid;
    grid-template-rows: 100px 104px 108px 104px;
    row-gap: 2px;
  }
  .banner--two .services,
  .banner--three .services {
    background: linear-gradient(160deg, var(--navy) 0%, var(--navy-deep) 100%);
  }
  .service {
    display: grid;
    grid-template-columns: 85px 1fr;
  }
  .service__icon-cell {
    background: var(--white);
    display: flex;
    align-items: center;
    justify-content: center;
  }
  .service__icon {
    width: 60px; height: 60px;
    border-radius: 50%;
    background: var(--navy);
    border: 2px solid var(--white);
    box-shadow: 0 0 0 1px #c9cbd3, 0 2px 4px rgba(0,0,0,.25);
  }
  .service__body { padding: 8px 8px 0 12px; }
  .service__title {
    font-weight: 600;
    font-size: 22px;
    line-height: 23px;
    text-transform: uppercase;
    color: var(--orange);
    margin-bottom: 4px;
  }
  .service__points { list-style: none; }
  .service__points li {
    position: relative;
    padding-left: 9px;
    font-weight: 500;
    font-size: 11px;
    line-height: 13.5px;
    color: var(--white);
    text-transform: uppercase;
    margin-bottom: 2px;
  }
  .service__points li::before {
    content: "";
    position: absolute;
    left: 1px; top: 5px;
    width: 4px; height: 4px;
    border-radius: 50%;
    background: var(--white);
  }

  .banner--two .service--content .service__title,
  .banner--three .service--content .service__title { color: var(--red); }
  .banner--two .service--curriculum .service__title,
  .banner--three .service--curriculum .service__title { color: var(--sky); }
  .banner--two .service--assessment .service__title,
  .banner--three .service--assessment .service__title { color: var(--yellow); }

  .banner__foot {
    height: 77px;
    display: grid;
    grid-template-columns: 85px 1fr;
  }
  .banner__foot-block { background: var(--navy); }
  .banner__url {
    display: flex;
    align-items: center;
    justify-content: center;
    background: var(--white);
    color: var(--navy);
    font-weight: 500;
    font-size: 11.5px;
    letter-spacing: .1px;
    box-shadow: inset 0 6px 6px -4px rgba(0,0,0,.25);
  }
  .banner--three .banner__url { background: var(--url-blue); color: var(--white); box-shadow: none; }
</style>
</head>
<body>

<div class="option-label label--one">Banner-1</div>
<div class="option-label label--two">Banner-2</div>
<div class="option-label label--three">Banner-3</div>

<!-- Option one -->
<section class="banner banner--one">
  <header class="banner__head">
    <div class="idea-bulbs" role="img" aria-label="Hanging crumpled-paper light bulbs in red, blue, yellow, orange and cyan"></div>
    <div class="brand"><span class="brand__name">DOLBROOK</span><span class="brand__tag">Teaching Advisory</span></div>
  </header>
  <div class="services">
    <div class="service service--content">
      <div class="service__icon-cell"><div class="service__icon" role="img" aria-label="Icon of a head with ideas and learning symbols"></div></div>
      <div class="service__body">
        <h2 class="service__title">Educational<br>Content Creation</h2>
        <ul class="service__points"><li>Supplemental textbook content<br>development</li><li>E-learning content development</li></ul>
      </div>
    </div>
    <div class="service service--curriculum">
      <div class="service__icon-cell"><div class="service__icon" role="img" aria-label="Icon of a teacher presenting charts on a board"></div></div>
      <div class="service__body">
        <h2 class="service__title">Curriculum<br>Development</h2>
        <ul class="service__points"><li>KVTR/Bright Ladder</li><li>Three dimensional learning</li></ul>
      </div>
    </div>
    <div class="service service--assessment">
      <div class="service__icon-cell"><div class="service__icon" role="img" aria-label="Icon of a flask surrounded by science symbols"></div></div>
      <div class="service__body">
        <h2 class="service__title">Assessment</h2>
        <ul class="service__points"><li>Formative assessments</li><li>Elementary school, middle school,<br>high school, college,<br>and business</li></ul>
      </div>
    </div>
    <div class="service service--professional">
      <div class="service__icon-cell"><div class="service__icon" role="img" aria-label="Icon of a hand holding a light bulb with growth symbols"></div></div>
      <div class="service__body">
        <h2 class="service__title">Professional<br>Development</h2>
        <ul class="service__points"><li>Training</li><li>Facilitation</li></ul>
      </div>
    </div>
  </div>
  <footer class="banner__foot"><div class="banner__foot-block"></div><div class="banner__url">WWW.DOLBROOKTEACHINGADVISORY.COM</div></footer>
</section>

<!-- Option two -->
<section class="banner banner--two">
  <header class="banner__head">
    <div class="idea-bulbs" role="img" aria-label="Hanging crumpled-paper light bulbs in red, blue, yellow, orange and cyan"></div>
    <div class="brand"><span class="brand__name">DOLBROOK</span><span class="brand__tag">Teaching Advisory</span></div>
  </header>
  <div class="services">
    <div class="service service--content">
      <div class="service__icon-cell"><div class="service__icon" role="img" aria-label="Icon of a head with ideas and learning symbols"></div></div>
      <div class="service__body">
        <h2 class="service__title">Educational<br>Content Creation</h2>
        <ul class="service__points"><li>Supplemental textbook content<br>development</li><li>E-learning content development</li></ul>
      </div>
    </div>
    <div class="service service--curriculum">
      <div class="service__icon-cell"><div class="service__icon" role="img" aria-label="Icon of a teacher presenting charts on a board"></div></div>
      <div class="service__body">
        <h2 class="service__title">Curriculum<br>Development</h2>
        <ul class="service__points"><li>KVTR/Bright Ladder</li><li>Three dimensional learning</li></ul>
      </div>
    </div>
    <div class="service service--assessment">
      <div class="service__icon-cell"><div class="service__icon" role="img" aria-label="Icon of a flask surrounded by science symbols"></div></div>
      <div class="service__body">
        <h2 class="service__title">Assessment</h2>
        <ul class="service__points"><li>Formative assessments</li><li>Elementary school, middle school,<br>high school, college,<br>and business</li></ul>
      </div>
    </div>
    <div class="service service--professional">
      <div class="service__icon-cell"><div class="service__icon" role="img" aria-label="Icon of a hand holding a light bulb with growth symbols"></div></div>
      <div class="service__body">
        <h2 class="service__title">Professional<br>Development</h2>
        <ul class="service__points"><li>Training</li><li>Facilitation</li></ul>
      </div>
    </div>
  </div>
  <footer class="banner__foot"><div class="banner__foot-block"></div><div class="banner__url">WWW.DOLBROOKTEACHINGADVISORY.COM</div></footer>
</section>

<!-- Option three -->
<section class="banner banner--three">
  <header class="banner__head">
    <div class="idea-bulbs" role="img" aria-label="Hanging crumpled-paper light bulbs in red, blue, yellow, orange and cyan on a chalkboard"></div>
    <div class="brand"><span class="brand__name">DOLBROOK</span><span class="brand__tag">Teaching Advisory</span></div>
  </header>
  <div class="services">
    <div class="service service--content">
      <div class="service__icon-cell"><div class="service__icon" role="img" aria-label="Icon of a head with ideas and learning symbols"></div></div>
      <div class="service__body">
        <h2 class="service__title">Educational<br>Content Creation</h2>
        <ul class="service__points"><li>Supplemental textbook content<br>development</li><li>E-learning content development</li></ul>
      </div>
    </div>
    <div class="service service--curriculum">
      <div class="service__icon-cell"><div class="service__icon" role="img" aria-label="Icon of a teacher presenting charts on a board"></div></div>
      <div class="service__body">
        <h2 class="service__title">Curriculum<br>Development</h2>
        <ul class="service__points"><li>KVTR/Bright Ladder</li><li>Three dimensional learning</li></ul>
      </div>
    </div>
    <div class="service service--assessment">
      <div class="service__icon-cell"><div class="service__icon" role="img" aria-label="Icon of a flask surrounded by science symbols"></div></div>
      <div class="service__body">
        <h2 class="service__title">Assessment</h2>
        <ul class="service__points"><li>Formative assessments</li><li>Elementary school, middle school,<br>high school, college,<br>and business</li></ul>
      </div>
    </div>
    <div class="service service--professional">
      <div class="service__icon-cell"><div class="service__icon" role="img" aria-label="Icon of a hand holding a light bulb with growth symbols"></div></div>
      <div class="service__body">
        <h2 class="service__title">Professional<br>Development</h2>
        <ul class="service__points"><li>Training</li><li>Facilitation</li></ul>
      </div>
    </div>
  </div>
  <footer class="banner__foot"><div class="banner__foot-block"></div><div class="banner__url">WWW.DOLBROOKTEACHINGADVISORY.COM</div></footer>
</section>

</body>
</html>
```